Postcard / Online add graphic

I'm doing a campaign and need a single design that I can put into different formats. I can do that part, I just need the creative part done.

Title: Feed the Social Media Monster with Great Photography
Content: You can take the content from my website: http://www.brindlelenswork.com/business-branding-photography/

Sample Images: https://www.parcelvault.net/sh/k7m2qx9wbtrflzc/QRT3H8k2pwmXcDdLbvHUen_5r?dl=0

Here is a Monster image I licensed for use for this project: https://www.parcelvault.net/s/4hw7ncr2lpzqvkd/stockorbit_xxl_technologymosters.jpg?dl=0

Logo is attached

I want it to be fun, colorful, graphical, and attention getting. Cartoonish is ok.

Target Market(s)

Business owners, social media managers

Industry/Entity Type

Campaign

Font styles to use
Sans Serif

Requirements
Must have
• Title and design on front
• Sales copy on back (whatever fits)
• Contact Information: Wade Pellinger, Photographer, (555) 314-7720, www.brindlelenswork.com

```html
<!DOCTYPE html>
<html lang="en">
<head>
<meta charset="utf-8">
<title>Feed the Social Media Monster – Postcard</title>
<link rel="stylesheet" href="https://fonts.googleapis.com/css2?family=Bebas+Neue&family=Oswald:wght@400;600;700&family=Great+Vibes&family=Jost:wght@400;500;700&family=Kaushan+Script&display=swap">
<style>
:root{
  --stage:#e9e6e1;
  --white:#ffffff;
  --ink:#1d1d1f;
  --ink-soft:#3a3a3c;
  --monster-red:#d9463a;
  --sky-top:#5f7d86;
  --sky-mid:#8aa3a0;
  --city:#2b3434;
  --teal:#4fc4b0;
  --coral:#e46a55;
  --band-blue:#dce9f6;
  --accent-blue:#8db4e2;
  --stamp:#b5b5b5;
  --thumb-a:#6f95b8;
  --thumb-b:#c9c3bb;
  --thumb-c:#a9856a;
  --thumb-d:#3f8f5a;
}
*{box-sizing:border-box;margin:0;padding:0}
html,body{width:1200px;height:778px;overflow:hidden;background:var(--stage)}
.canvas{position:relative;width:1200px;height:778px}

/* ---------- FRONT ---------- */
.card{position:absolute;width:570px;height:400px;overflow:hidden;box-shadow:0 6px 18px rgba(0,0,0,.18)}
.card--front{left:20px;top:189px}
.front-art{position:absolute;inset:0;
  background:
    linear-gradient(180deg,transparent 68%,var(--city) 100%),
    radial-gradient(ellipse 130px 170px at 470px 200px,var(--teal) 0 95%,transparent 100%),
    radial-gradient(ellipse 80px 120px at 300px 250px,var(--coral) 0 95%,transparent 100%),
    linear-gradient(180deg,var(--sky-top) 0%,var(--sky-mid) 55%,#4b5a58 100%)}
.headline{position:absolute;left:40px;top:24px;width:170px;color:var(--white);text-align:center}
.headline span{display:block}
.headline__feed{font-family:"Bebas Neue",sans-serif;font-size:84px;line-height:.85;letter-spacing:1px}
.headline__social{font-family:"Oswald",sans-serif;font-weight:600;font-size:21px;line-height:1.1;margin-top:6px}
.headline__monster{font-family:"Oswald",sans-serif;font-weight:700;font-size:30px;line-height:1;color:var(--monster-red);letter-spacing:1px;margin-top:4px}
.headline__with{font-family:"Oswald",sans-serif;font-size:11px;line-height:1.2;letter-spacing:3px;margin-top:3px;position:relative;z-index:1}
.headline__great{font-family:"Great Vibes",cursive;font-size:54px;line-height:1;margin-top:2px}
.headline__photo{font-family:"Oswald",sans-serif;font-weight:600;font-size:22px;line-height:1.2;margin-top:2px;padding-bottom:5px;border-bottom:2px solid var(--white)}
.front-brand{position:absolute;right:22px;bottom:30px;color:var(--white);font-family:"Jost",sans-serif;font-weight:500;font-size:15px;letter-spacing:2px;text-transform:uppercase}

/* ---------- BACK ---------- */
.card--back{left:610px;top:189px;background:var(--white)}
.back-band{position:absolute;left:0;top:0;width:100%;height:100%}
.back-header{position:absolute;left:16px;top:14px;display:flex;align-items:center;gap:12px;font-family:"Jost",sans-serif}
.back-header__brand{font-family:"Jost",sans-serif;font-weight:500;font-size:18px;letter-spacing:2px;color:var(--ink);width:190px;text-transform:uppercase}
.back-header__rule{width:1px;height:38px;background:var(--ink)}
.back-header__person{font-size:8px;text-align:center;color:var(--ink-soft);line-height:1.6}
.back-header__person strong{display:block;font-size:9px;color:var(--ink)}
.back-header__contact{font-size:7px;line-height:1.35;color:var(--ink-soft)}
.back-header__contact strong{color:var(--ink);font-weight:700}
.stamp{position:absolute;right:14px;top:12px;width:92px;height:80px;background:var(--stamp)}
.back-copy{position:absolute;left:20px;top:100px;width:370px;font-family:"Jost",sans-serif;color:var(--ink)}
.back-copy h2{font-family:"Oswald",sans-serif;font-weight:700;font-size:13px;letter-spacing:.2px;margin-bottom:4px}
.back-copy ul{font-size:8.5px;padding-left:22px;line-height:1.35;margin-bottom:12px}
.back-copy p{font-size:7.6px;line-height:1.4}
.gallery{position:absolute;left:22px;top:258px;display:flex;gap:6px}
.gallery figure{width:68px}
.gallery .thumb{height:54px}
.gallery figcaption{font-family:"Jost",sans-serif;font-weight:700;font-size:6.5px;line-height:1.15;margin-top:5px;color:var(--ink);padding-left:4px}
.thumb--a{background:linear-gradient(160deg,var(--thumb-a),#a4c0d8)}
.thumb--b{background:linear-gradient(160deg,var(--thumb-b),#e8e4de)}
.thumb--c{background:linear-gradient(160deg,var(--thumb-c),#e4d2c4)}
.thumb--d{background:linear-gradient(160deg,var(--thumb-d),#d9dee0)}
.cta{position:absolute;left:14px;bottom:8px;font-family:"Kaushan Script",cursive;font-size:12.5px;line-height:1.25;color:var(--white)}
</style>
</head>
<body>
<main class="canvas">

  <section class="card card--front" aria-label="Postcard front">
    <div class="front-art" role="img" aria-label="Two cartoon phone and tablet monsters with big eyes and toothy grins rising over a city skyline under a cloudy sky"></div>
    <h1 class="headline">
      <span class="headline__feed">FEED</span>
      <span class="headline__social">THE SOCIAL MEDIA</span>
      <span class="headline__monster">MONSTER</span>
      <span class="headline__with">WITH</span>
      <span class="headline__great">Great</span>
      <span class="headline__photo">PHOTOGRAPHY</span>
    </h1>
    <div class="front-brand">Pellinger Photography</div>
  </section>

  <section class="card card--back" aria-label="Postcard back">
    <svg class="back-band" viewBox="0 0 570 400" aria-hidden="true">
      <defs>
        <linearGradient id="bandFill" x1="0" y1="0" x2="0" y2="1">
          <stop offset="0" stop-color="#dce9f6"/>
          <stop offset="0.55" stop-color="#eef3f6"/>
          <stop offset="1" stop-color="#f6f7f5"/>
        </linearGradient>
      </defs>
      <polygon points="0,0 420,0 250,400 0,400" fill="url(#bandFill)"/>
      <polygon points="0,366 198,366 184,400 0,400" fill="var(--accent-blue)"/>
      <polygon points="0,352 210,352 198,366 0,366" fill="var(--accent-blue)" opacity=".75"/>
    </svg>
    <div role="img" aria-label="Faded desert landscape with saguaro cacti and distant mountains" style="position:absolute;left:0;top:110px;width:330px;height:170px;background:linear-gradient(180deg,rgba(150,170,180,.18),rgba(120,140,120,.14));clip-path:polygon(0 0,100% 0,80% 100%,0 100%)"></div>

    <header class="back-header">
      <div class="back-header__brand">Pellinger Photography</div>
      <span class="back-header__rule"></span>
      <div class="back-header__person"><strong>Wade Pellinger</strong>PHOTOGRAPHER</div>
      <span class="back-header__rule"></span>
      <div class="back-header__contact"><strong>(555) 314-7720</strong><br><strong>www.brindlelenswork.com</strong><br>Pellinger Photography<br>1420 W. Larkspur Ave Ste 310<br>Marlow, AZ 85099</div>
    </header>
    <div class="stamp" aria-label="Postage area"></div>

    <article class="back-copy">
      <h2>WHAT CAN BUSINESS BRANDIGN PHOTOGRAPHY DO FOR YOU?</h2>
      <ul>
        <li>It tells your story in a fun, highly visual way</li>
        <li>It tells your story in a fun, highly visual way</li>
        <li>It tells your story in a fun, highly visual way</li>
      </ul>
      <h2>HOW DOES IT WORK?</h2>
      <p>"Lorem ipsum dolor sit amet, consectetur adipiscing elit, sed do eiusmod tempor incididunt ut labore et dolore magna aliqua. Ut enim ad minim veniam, quis nostrud exercitation ullamco laboris nisi ut aliquip ex ea commodo consequat. Duis aute irure dolor in reprehenderit in voluptate velit esse cillum dolore eu fugiat nulla pariatur. Excepteur sint occaecat cupidatat non proident, sunt in culpa qui officia deserunt mollit anim id est laborum."</p>
    </article>

    <div class="gallery">
      <figure><div class="thumb thumb--a" role="img" aria-label="Business owner portrait in front of a billboard"></div><figcaption>Business<br>Branding<br>Phography</figcaption></figure>
      <figure><div class="thumb thumb--b" role="img" aria-label="Restaurant interior and counter"></div><figcaption>Real<br>State<br>phography</figcaption></figure>
      <figure><div class="thumb thumb--c" role="img" aria-label="Baker holding a plated dessert"></div><figcaption>Portraits &amp;<br>headshots</figcaption></figure>
      <figure><div class="thumb thumb--d" role="img" aria-label="Staff member in a green shop apron"></div><figcaption>Product<br>phography</figcaption></figure>
    </div>

    <p class="cta">Contact me to book your Shoot!<br>Your satisfaction is guaranteed!</p>
  </section>

</main>
</body>
</html>
```